Polling website project

We need a website design for a polling website called vextiq.com. This will be a website where visitors can take and create polls for various topics along with view results. We want something really simple and "web 2.0." We are going to make a cell phone app that goes along with the website and we want the look and feel of the website to be very "app-like." Basically that means minimalistic design with a poll being the center of the page.
When someone comes to the site, we want them to see basically just a poll in the center of the screen and a toolbar at the top of the page with links to login fields/user profile, post a new poll, view friends list, a drop-down list of poll topics, and a search bar. We need about three pages mocked up: a home page/poll view page, a user control panel/profile page, a submit new poll page.
We also want our logo/header to have a "pulse" theme. The name vextiq is supposed to be a play on the word pulse, we'd like the logo to make that obvious, maybe the use of the EKG graph could work.
We also want a nice tab in the corner to sign up that is attractive and flashy, kind of like the feedback tab on the side of this website.
Target Market(s)
Teens and young adults, the chatterloop crowd
Industry/Entity Type
Cell Phone
Look and feel
Each slider illustrates characteristics of the customer's brand and the style your logo design should communicate.

```html
<!DOCTYPE html>
<html lang="en">
<head>
<meta charset="utf-8">
<title>vextiq – How often do people orgasm?</title>
<link href="https://fonts.googleapis.com/css2?family=Arimo:ital,wght@0,400;0,700;1,400&display=swap" rel="stylesheet">
<style>
  :root {
    --page: #f1f1f1;
    --nav: #b9babd;
    --logo-block: #808184;
    --sky: #abdcf5;
    --ink: #231f20;
    --white: #ffffff;
    --grey-1: #3d3d3f;
    --grey-2: #58595b;
    --grey-3: #6d6e71;
    --grey-4: #939598;
    --grey-5: #a7a9ac;
    --rule: #8c8d90;
  }
  * { box-sizing: border-box; margin: 0; padding: 0; }
  html, body { width: 1200px; height: 851px; overflow: hidden; }
  body { background: var(--page); font-family: "Arimo", Helvetica, Arial, sans-serif; color: var(--ink); position: relative; }

  .site { position: absolute; left: 5px; top: 40px; width: 933px; height: 808px; background: var(--sky); border-bottom: 3px solid var(--rule); }

  .topbar { position: absolute; left: 0; top: 0; width: 933px; height: 100px; background: var(--nav); }
  .nav-group { position: absolute; top: 0; height: 100px; display: flex; flex-direction: column; justify-content: center; }
  .nav-group a { color: var(--white); text-decoration: none; font-size: 17px; letter-spacing: .3px; text-align: center; line-height: 40px; }
  .nav-left { left: 14px; width: 229px; }
  .nav-right { left: 690px; width: 228px; }
  .nav-group a + a { border-top: 1.5px solid var(--white); }

  .logo-block { position: absolute; left: 256px; top: -32px; width: 420px; height: 132px; background: var(--logo-block); display: flex; align-items: center; justify-content: center; padding-top: 12px; }
  .logo-block span { color: var(--white); font-size: 31px; letter-spacing: .5px; }

  .question { position: absolute; left: 30px; top: 141px; display: flex; align-items: center; gap: 22px; font-weight: 700; font-size: 19.5px; }
  .divider { position: absolute; left: 426px; top: 110px; width: 1.5px; height: 98px; background: var(--ink); }

  .formula { position: absolute; left: 461px; top: 122px; display: flex; align-items: center; }
  .pct-box { width: 37px; height: 38px; background: var(--ink); color: var(--white); font-weight: 700; font-size: 19px; display: flex; align-items: center; justify-content: center; }
  .equals { margin: 0 14px 0 15px; }
  .fraction { width: 171px; text-align: center; font-weight: 700; font-size: 19px; }
  .fraction .top { padding-bottom: 5px; border-bottom: 2px solid var(--ink); }
  .fraction .bottom { padding-top: 6px; }

  .donut { position: absolute; left: 50px; top: 250px; }
  .donut text { font-family: "Arimo", Helvetica, Arial, sans-serif; }

  .us-map { position: absolute; left: 437px; top: 270px; width: 460px; height: 275px; background: linear-gradient(135deg, #8c8d90, #6d6e71); border-radius: 18px 30px 40px 60px; }

  .share { position: absolute; top: 528px; width: 90px; height: 90px; border-radius: 50%; background: var(--ink); color: var(--white); font-weight: 700; font-size: 38px; display: flex; align-items: center; justify-content: center; letter-spacing: -1px; }
  .share sup { font-size: 15px; margin-top: -14px; margin-left: 1px; }
  .share-a { left: 233px; }
  .share-b { left: 343px; }
  .figure { position: absolute; top: 616px; width: 76px; height: 120px; background: var(--white); border: 2.5px solid var(--ink); border-radius: 20px 20px 6px 6px; }
  .figure-a { left: 240px; }
  .figure-b { left: 350px; }

  .age-bars { position: absolute; left: 552px; top: 568px; list-style: none; }
  .age-bars li { height: 26px; margin-bottom: 10px; display: flex; align-items: center; padding-left: 8px; font-weight: 700; font-size: 16px; }
  .age-bars .b1 { width: 73px; background: var(--grey-4); color: var(--ink); }
  .age-bars .b2 { width: 118px; background: var(--grey-5); color: var(--ink); margin-top: 12px; }
  .age-bars .b3 { width: 171px; background: var(--grey-2); color: #c9cacc; height: 25px; }
  .age-bars .b4 { width: 217px; background: var(--grey-1); color: #c9cacc; height: 24px; }
  .age-bars .b5 { width: 55px; background: var(--white); color: var(--ink); height: 25px; }
</style>
</head>
<body>
<main class="site">
  <header class="topbar">
    <nav class="nav-group nav-left"><a href="#">CATEGORIES</a><a href="#">SUBMIT QUESTION</a></nav>
    <div class="logo-block"><span>LOGO</span></div>
    <nav class="nav-group nav-right"><a href="#">SIGN UP / SIGN IN</a><a href="#">FRIEND’S LIST</a></nav>
  </header>

  <h1 class="question">
    <svg width="32" height="22" viewBox="0 0 32 22" aria-hidden="true"><path d="M1 11H29M19 2L29 11L19 20" fill="none" stroke="#231f20" stroke-width="2.8"/></svg>
    How often do people orgasm?
  </h1>
  <div class="divider"></div>

  <div class="formula">
    <div class="pct-box">%</div>
    <svg class="equals" width="24" height="14" viewBox="0 0 24 14" aria-hidden="true"><rect x="0" y="0" width="24" height="5" rx="2" fill="#231f20"/><rect x="0" y="9" width="24" height="5" rx="2" fill="#231f20"/></svg>
    <div class="fraction"><div class="top">orgasm</div><div class="bottom"># of sex</div></div>
  </div>

  <svg class="donut" width="310" height="260" viewBox="0 0 310 260" aria-label="Donut chart of percent of the time">
    <g transform="rotate(-100 149 130)" fill="none" stroke-width="25">
      <circle cx="149" cy="130" r="91" stroke="#231f20" stroke-dasharray="15.9 571.8" stroke-dashoffset="0"/>
      <circle cx="149" cy="130" r="91" stroke="#58595b" stroke-dasharray="79.4 571.8" stroke-dashoffset="-15.9"/>
      <circle cx="149" cy="130" r="91" stroke="#6d6e71" stroke-dasharray="238.2 571.8" stroke-dashoffset="-95.3"/>
      <circle cx="149" cy="130" r="91" stroke="#a7a9ac" stroke-dasharray="119.1 571.8" stroke-dashoffset="-333.5"/>
      <circle cx="149" cy="130" r="91" stroke="#ffffff" stroke-dasharray="119.1 571.8" stroke-dashoffset="-452.6"/>
    </g>
    <circle cx="149" cy="130" r="77" fill="none" stroke="#231f20" stroke-width="5"/>
    <text x="149" y="125" text-anchor="middle" font-weight="700" font-size="24" fill="#231f20">%</text>
    <text x="149" y="141" text-anchor="middle" font-style="italic" font-size="17" fill="#231f20">of the time</text>
    <g font-weight="700" font-size="17" fill="#231f20">
      <text x="114" y="13">100</text>
      <text x="196" y="22">75</text>
      <text x="266" y="164">50</text>
      <text x="90" y="254">25</text>
      <text x="22" y="98">0</text>
    </g>
  </svg>

  <div class="us-map" role="img" aria-label="Map of the United States shaded by state in greys"></div>

  <div class="share share-a">75<sup>%</sup></div>
  <div class="share share-b">25<sup>%</sup></div>
  <div class="figure figure-a" role="img" aria-label="Outline figure of a man"></div>
  <div class="figure figure-b" role="img" aria-label="Outline figure of a woman"></div>

  <ul class="age-bars">
    <li class="b1">←18</li>
    <li class="b2">18→29</li>
    <li class="b3">30→45</li>
    <li class="b4">50→64</li>
    <li class="b5">65→</li>
  </ul>
</main>
</body>
</html>
```